Harbourline Group needs a business card design

Business card should represent civil engineering infrastructure projects such as roads, bridges, tunnels, rail, rail, pipelines, structures and resource infrastructure

Industry/Entity Type

Business

```html
<!DOCTYPE html>
<html lang="en">
<head>
<meta charset="utf-8">
<title>Harbourline Group – Business Card</title>
<link rel="stylesheet" href="https://fonts.googleapis.com/css2?family=Oswald:wght@300;400;500&family=Arimo&display=swap">
<style>
  :root {
    --backdrop: #3b3533;
    --card-light: #eceee9;
    --card-light-edge: #d3d6cf;
    --navy: #2b2a86;
    --navy-deep: #1a1560;
    --gold: #e2b53a;
    --gold-dark: #8a6a1c;
    --gold-pale: #fff3a8;
    --ink: #111111;
    --white: #ffffff;
    --cream: #fbf5d6;
    --charcoal: #4a4f4b;
    --charcoal-deep: #0c100d;
    --label: #d8d8d8;
  }
  * { margin: 0; padding: 0; box-sizing: border-box; }
  html, body { width: 1000px; height: 1200px; overflow: hidden; }
  body {
    background: var(--backdrop);
    font-family: "Oswald", sans-serif;
    position: relative;
  }
  .card {
    position: absolute;
    width: 740px;
    height: 457px;
    overflow: hidden;
  }
  .card--front { left: 132px; top: 119px; background: radial-gradient(ellipse at 50% 20%, var(--card-light) 30%, var(--card-light-edge) 100%); }
  .card--back { left: 117px; top: 665px; height: 456px; background: radial-gradient(ellipse at 50% 45%, var(--charcoal) 0%, #262b28 45%, var(--charcoal-deep) 100%); }
  .card__waves { position: absolute; inset: 0; }
  .brand {
    position: absolute;
    display: flex;
    align-items: center;
    gap: 18px;
  }
  .brand__dot { width: 70px; height: 70px; border-radius: 50%; background: var(--gold); }
  .brand__name { font-weight: 400; line-height: 1; }
  .card--front .brand { left: 300px; top: 100px; }
  .card--front .brand__name { font-size: 68px; color: var(--ink); }
  .card--back .brand { left: 0; right: 0; top: 105px; flex-direction: column; gap: 30px; }
  .card--back .brand__name { font-size: 72px; color: var(--cream); }
  .card--back .brand__dot { width: 90px; height: 90px; }
  .web-email {
    position: absolute;
    left: 0; right: 0;
    text-align: center;
  }
  .card--front .web-email { top: 233px; font-size: 22px; font-weight: 500; color: var(--ink); }
  .card--back .web-email { top: 334px; font-size: 20px; font-weight: 300; color: var(--cream); }
  .person { position: absolute; left: 43px; top: 335px; }
  .person__name { font-size: 24px; font-weight: 400; color: var(--gold); line-height: 1.3; }
  .person__role { font-size: 19px; font-weight: 400; color: var(--white); line-height: 1.5; }
  .contact { position: absolute; right: 44px; top: 339px; list-style: none; text-align: right; }
  .contact__item { font-size: 18px; font-weight: 300; color: var(--white); line-height: 32px; display: flex; align-items: center; justify-content: flex-end; gap: 6px; }
  .contact__icon { width: 16px; height: 16px; }
  .side-label { position: absolute; font-family: "Arimo", sans-serif; font-size: 20px; color: var(--label); }
</style>
</head>
<body>
  <section class="card card--front" aria-label="Card front">
    <svg class="card__waves" viewBox="0 0 740 457" aria-hidden="true">
      <defs>
        <linearGradient id="navyFill" x1="0" y1="0" x2="1" y2="0">
          <stop offset="0" stop-color="#322f92"/>
          <stop offset="1" stop-color="#1a1560"/>
        </linearGradient>
        <linearGradient id="goldLine" x1="0" y1="0" x2="1" y2="0">
          <stop offset="0" stop-color="#5a4512"/>
          <stop offset="0.5" stop-color="#8a6a1c"/>
          <stop offset="0.85" stop-color="#f0d040"/>
          <stop offset="1" stop-color="#fff3a8"/>
        </linearGradient>
      </defs>
      <path d="M0,200 Q330,400 740,212 L740,457 L0,457 Z" fill="url(#navyFill)"/>
      <path d="M0,200 Q330,400 740,212 L740,238 Q360,380 0,214 Z" fill="#f4f4f0"/>
      <path d="M0,200 Q330,400 740,206" fill="none" stroke="url(#goldLine)" stroke-width="5"/>
    </svg>
    <div class="brand">
      <span class="brand__dot"></span>
      <span class="brand__name">HLG</span>
    </div>
    <p class="web-email">ian.colby@harbourlinegroup.com.au</p>
    <div class="person">
      <p class="person__name">OWEN HARTLEY</p>
      <p class="person__role">Business Manager</p>
    </div>
    <ul class="contact">
      <li class="contact__item">ian.r.colby@mailnet.com
        <svg class="contact__icon" viewBox="0 0 16 16" aria-hidden="true"><rect x="1" y="4" width="14" height="9" fill="var(--gold)"/><path d="M1,4 L8,9.5 L15,4" fill="none" stroke="#1a1560" stroke-width="1.2"/></svg>
      </li>
      <li class="contact__item">+61400123456
        <svg class="contact__icon" viewBox="0 0 16 16" aria-hidden="true"><path d="M4,2 L6.5,2 L7.5,5.5 L6,7 Q7.5,9.5 9,10.5 L10.5,9 L14,10 L14,12.5 Q12,14.5 9,13 Q4,10 2.5,5.5 Q2,3 4,2 Z" fill="var(--gold)"/></svg>
      </li>
    </ul>
  </section>
  <p class="side-label" style="left:139px; top:590px;">Front</p>

  <section class="card card--back" aria-label="Card back">
    <div class="brand">
      <span class="brand__name">HLG</span>
      <span class="brand__dot"></span>
    </div>
    <p class="web-email">ian.colby@harbourlinegroup.com.au</p>
  </section>
  <p class="side-label" style="left:799px; top:1140px;">Back</p>
</body>
</html>
```